Real Estate Sales Brokerage

Design a modern and fresh looking standard size business card, incorporate our logo's color scheme and modern appearance with head shot photo on front side and incorporate our log on the back side

Target Market(s)

Residential Home sales

Industry/Entity Type

Real Estate Agent

Font styles to use
Sans Serif

Colors

Designer to choose colors to be used in the design.

Requirements
Must have
• fresh, modern, not too busy, incorporate head shot in front of the card, incorporate logo in front and back of the card. Use logo design scheme as appropriate.
Nice to have
• horizontal and vertical options to compare would be nice.

```html
<!DOCTYPE html>
<html lang="en">
<head>
<meta charset="utf-8">
<title>Keystone Hearth Realty – Business Card</title>
<link href="https://fonts.googleapis.com/css2?family=Cinzel:wght@500;600&family=Crimson+Text:wght@400&display=swap" rel="stylesheet">
<style>
  :root {
    --olive: #5c5c2b;
    --gold: #e6c53c;
    --paper: #f5f5f2;
    --ink: #1f1f1f;
    --backdrop: #8e8e8e;
    --photo-top: #c9cfd6;
    --photo-bottom: #2e4c86;
  }
  * { box-sizing: border-box; margin: 0; padding: 0; }
  html, body { width: 1200px; height: 1200px; overflow: hidden; }
  body {
    background: var(--backdrop);
    font-family: "Crimson Text", Georgia, serif;
    color: var(--ink);
    position: relative;
  }
  .card {
    position: absolute;
    left: 180px;
    width: 840px;
    height: 480px;
    background: var(--paper);
    overflow: hidden;
    box-shadow: 0 10px 24px rgba(0,0,0,.25);
  }
  .card--front { top: 100px; }
  .card--back { top: 620px; }
  .card__bands { position: absolute; inset: 0; width: 100%; height: 100%; }

  .headshot {
    position: absolute;
    left: 24px; top: 50px;
    width: 300px; height: 300px;
    background: linear-gradient(180deg, var(--photo-top) 0%, var(--paper) 30%, var(--photo-bottom) 55%, var(--photo-bottom) 100%);
  }

  .brand {
    position: absolute;
    display: flex;
    align-items: center;
    gap: 12px;
    font-family: "Cinzel", "Times New Roman", serif;
    font-weight: 600;
    line-height: 1.05;
    letter-spacing: .04em;
  }
  .brand__mark { width: 34px; height: 34px; flex: none; }
  .brand--front { left: 500px; top: 50px; color: var(--olive); font-size: 24px; }
  .brand--front .brand__mark { background: var(--olive); }
  .brand--back { left: 60px; top: 330px; color: var(--paper); font-size: 24px; }
  .brand--back .brand__mark { background: var(--paper); }

  .agent { position: absolute; left: 370px; top: 142px; z-index: 1; }
  .agent__name {
    font-family: "Cinzel", "Times New Roman", serif;
    font-weight: 500;
    font-size: 30px;
    line-height: 1.2;
    letter-spacing: .06em;
  }
  .agent__title { font-size: 19px; line-height: 1.1; }
  .contact {
    list-style: none;
    margin-top: 10px;
    font-size: 19px;
    line-height: 1.25;
  }
  .contact li { display: flex; }
  .contact__key { width: 36px; flex: none; }
</style>
</head>
<body>

<section class="card card--front" aria-label="Business card front">
  <div class="headshot" role="img" aria-label="Agent head shot photo: man in a navy suit and red tie"></div>
  <svg class="card__bands" viewBox="0 0 840 480" preserveAspectRatio="none" aria-hidden="true">
    <path d="M300 349 C440 361 540 373 660 394 C540 378 440 366 300 349 Z" fill="var(--gold)"/>
    <path d="M0 345 C300 355 560 395 840 410 L840 480 L0 480 Z" fill="var(--olive)"/>
  </svg>
  <div class="brand brand--front">
    <span class="brand__mark"></span>
    <span>Keystone<br>Hearth<br>Realty</span>
  </div>
  <div class="agent">
    <h1 class="agent__name">Your Full Name</h1>
    <p class="agent__title">Your Tittle</p>
    <ul class="contact">
      <li><span class="contact__key">A :</span><span>Your address line 1<br>Your address line 2</span></li>
      <li><span class="contact__key">P :</span><span>012.345.6789</span></li>
      <li><span class="contact__key">E :</span><span>Your email@yourdomain.com</span></li>
      <li><span class="contact__key">W :</span><span>www.yourdomain.com</span></li>
    </ul>
  </div>
</section>

<section class="card card--back" aria-label="Business card back">
  <svg class="card__bands" viewBox="0 0 840 480" preserveAspectRatio="none" aria-hidden="true">
    <path d="M180 250 C420 262 620 280 820 300 C620 272 400 256 180 250 Z" fill="var(--gold)"/>
    <path d="M0 245 C300 255 560 280 840 300 L840 480 L0 480 Z" fill="var(--olive)"/>
  </svg>
  <div class="brand brand--back">
    <span class="brand__mark"></span>
    <span>Keystone<br>Hearth<br>Realty</span>
  </div>
</section>

</body>
</html>
```